Vital Spark Electrical in need of a business card design

We need a new business card designed for our electrical business. We have a logo already which I will attach below.
Would like the business card to be..
-BLACK background preferably, possibly white back ground behind logo if colours clash.
-White & Blue (logo blue) text
Something that makes the logo pop, & a modern look. Possibly minimal clean format.

REQUIRE:
-Logo on front & back

TEXT TO INCLUDE (ON ONE SIDE):

Tom Harlow
Director/Electrician
M: 0417 365 208
E:info@vitalsparkelectrical-example.com.au
W:www.vitalsparkelectrical-example.com.au
R.E.C 57318

Custom/New Homes
Renovations
Commercial Office/Shop Fit-outs
Communications & Security Cameras
Electric Vehicle Chargers
Airconditioning
Updates

Requirements
Nice to have
• Possibly even lighten the grey shades for the words 'Vital' & 'Spark' to be more easily read on a black background.

```html
<!DOCTYPE html>
<html lang="en">
<head>
<meta charset="utf-8">
<title>Vital Spark Electrical – Business Card</title>
<link href="https://fonts.googleapis.com/css2?family=Open+Sans:wght@300;400;600;700&display=swap" rel="stylesheet">
<style>
  :root {
    --stage: #2a2a2c;
    --card: #141414;
    --white: #f2f2f2;
    --grey: #c9c9c9;
    --blue: #1aa3e0;
  }
  * { box-sizing: border-box; margin: 0; padding: 0; }
  html, body { width: 1200px; height: 900px; overflow: hidden; }
  body {
    background: var(--stage);
    font-family: "Open Sans", Arial, sans-serif;
    color: var(--white);
    position: relative;
  }
  .card {
    position: absolute;
    left: 250px;
    width: 700px;
    height: 400px;
    background: var(--card);
    box-shadow: 0 10px 30px rgba(0,0,0,.45);
  }
  .card--front { top: 35px; }
  .card--back { top: 465px; }

  .brand {
    position: absolute;
    display: flex;
    align-items: center;
    gap: 14px;
  }
  .brand__mark {
    width: 26px; height: 26px;
    background: var(--blue);
    flex: none;
  }
  .brand__name {
    font-weight: 600;
    color: var(--white);
    white-space: nowrap;
  }

  /* front: contact side */
  .person { position: absolute; left: 50px; top: 50px; }
  .person__name {
    color: var(--blue);
    font-weight: 700;
    font-size: 26px;
    letter-spacing: .5px;
    text-transform: uppercase;
  }
  .person__role { font-weight: 300; font-size: 17px; margin-top: 2px; color: var(--grey); }
  .card--front .brand { right: 50px; top: 165px; }
  .card--front .brand__name { font-size: 30px; }

  .contact {
    position: absolute;
    right: 50px; bottom: 40px;
    text-align: right;
    font-weight: 300;
    font-size: 16px;
    line-height: 1.55;
  }
  .contact__licence { color: var(--blue); font-size: 17px; margin-bottom: 18px; }
  .contact__row { display: flex; align-items: center; justify-content: flex-end; gap: 10px; }
  .contact__row svg { width: 15px; height: 15px; flex: none; }

  /* back: logo + services */
  .card--back .brand { left: 50%; top: 120px; transform: translateX(-50%); }
  .card--back .brand__name { font-size: 40px; }
  .services {
    position: absolute;
    left: 40px; right: 40px; top: 235px;
    text-align: center;
    font-weight: 300;
    font-size: 15.5px;
    line-height: 1.7;
    color: var(--white);
  }
  .services .dot { color: var(--blue); margin: 0 6px; }
</style>
</head>
<body>

<section class="card card--front" aria-label="Business card front">
  <div class="person">
    <p class="person__name">Tom Harlow</p>
    <p class="person__role">Director/Electrician</p>
  </div>

  <div class="brand">
    <span class="brand__mark"></span>
    <span class="brand__name">Vital Spark Electrical</span>
  </div>

  <div class="contact">
    <p class="contact__licence">R.E.C 57318</p>
    <p class="contact__row">0417 365 208
      <svg viewBox="0 0 16 16"><path fill="var(--blue)" d="M4 1.5l2.3 3-1.4 1.6c.8 1.8 2.2 3.2 4 4l1.6-1.4 3 2.3-1.3 2.3C7 13.3 2.7 9 2 3.3z"/></svg>
    </p>
    <p class="contact__row">info@vitalsparkelectrical-example.com.au
      <svg viewBox="0 0 16 16"><rect x="1.5" y="3.5" width="13" height="9" fill="var(--blue)"/><path d="M1.5 3.5l6.5 5 6.5-5" fill="none" stroke="var(--card)" stroke-width="1.3"/></svg>
    </p>
    <p class="contact__row">www.vitalsparkelectrical-example.com.au
      <svg viewBox="0 0 16 16"><circle cx="8" cy="8" r="6.5" fill="none" stroke="var(--blue)" stroke-width="1.5"/><path d="M1.5 8h13M8 1.5c-3 3.5-3 9.5 0 13M8 1.5c3 3.5 3 9.5 0 13" fill="none" stroke="var(--blue)" stroke-width="1.2"/></svg>
    </p>
  </div>
</section>

<section class="card card--back" aria-label="Business card back">
  <div class="brand">
    <span class="brand__mark"></span>
    <span class="brand__name">Vital Spark Electrical</span>
  </div>
  <p class="services">
    Custom/New Homes<span class="dot">•</span>Renovations<span class="dot">•</span>Commercial Office/Shop Fit-outs<br>
    Communications &amp; Security Cameras<span class="dot">•</span>Electric Vehicle Chargers<span class="dot">•</span>Airconditioning
  </p>
</section>

</body>
</html>
```